Simple Logo Design for Semi-Clear Plastic Frosted Card stock

Create a business card on frosted plastic. compliment existing logo elements with a tree trunk, roots, or seed at the lower half and the full logo both on the front.

Contact information will go on a solid portion of the back of this design since this card stock is semi-transparent.

It is important to consider this plastic card stock medium in your design. I found helpful tips and guides listed at velnacard.example: be careful to understand ink printed on plastic cards cannot have too much of a consistent print area or risks peeling and fine lines can easily scratch off.
Updates

2" x 3.5" 20PT Clear Plastic Business cards with Round corners Please get info or templates here: https://www.velnacard.example/product-detail/2-x-35-20pt-clear-plastic-business-cards-with-round-corners

Target Market(s)

Not for profit- religion

Industry/Entity Type

Business

Contact Information for Business Card

Must include complementary elements to the existing logo

Font styles to use
Decorative

Colors
000000

Requirements
Must have
• Elements of community, nature and oneness. Such as: seed, roots, tree trunk, etc.
• Three lines of space on the back for Name, Title, Phone Number.
Nice to have
• I like a light use of decorative elements
Should not have
• No eyes, from faces or animals.

```html
<!DOCTYPE html>
<html lang="en">
<head>
<meta charset="utf-8">
<title>Kindred Grove – Business Card</title>
<link href="https://fonts.googleapis.com/css2?family=Questrial&family=Open+Sans:wght@400;600&display=swap" rel="stylesheet">
<style>
  :root {
    --backdrop: #e4e6e8;
    --card: #ffffff;
    --teal: #1f6b66;
    --leaf: #3f9a3c;
    --ink: #111111;
    --faint-leaf: #d7e8d2;
    --faint-trunk: #d5e1e3;
    --shadow: rgba(0, 0, 0, 0.14);
  }
  * { box-sizing: border-box; margin: 0; padding: 0; }
  html, body {
    width: 1200px;
    height: 864px;
    overflow: hidden;
    background: var(--backdrop);
  }
  .stage {
    position: relative;
    width: 1200px;
    height: 864px;
  }
  .card {
    position: absolute;
    width: 600px;
    height: 343px;
    background: var(--card);
    border-radius: 16px;
    box-shadow: 0 6px 18px var(--shadow);
    overflow: hidden;
  }
  .card--front { left: 300px; top: 60px; }
  .card--back  { left: 300px; top: 460px; }

  /* Front */
  .front-brand {
    position: absolute;
    inset: 0;
    display: flex;
    align-items: center;
    justify-content: center;
    gap: 16px;
  }
  .brand-dot {
    width: 34px;
    height: 34px;
    border-radius: 50%;
    background: var(--leaf);
  }
  .brand-name {
    font-family: "Questrial", sans-serif;
    font-size: 42px;
    letter-spacing: 1px;
    color: var(--teal);
    text-transform: uppercase;
  }

  /* Back */
  .back-brand {
    position: absolute;
    left: 48px;
    top: 34px;
    font-family: "Questrial", sans-serif;
    font-size: 34px;
    letter-spacing: 1px;
    color: var(--teal);
    text-transform: uppercase;
  }
  .contact {
    position: absolute;
    left: 48px;
    top: 140px;
    font-family: "Open Sans", sans-serif;
    color: var(--ink);
  }
  .contact-name {
    font-size: 19px;
    font-weight: 600;
    color: var(--teal);
  }
  .contact-title {
    font-size: 14px;
    margin-top: 2px;
  }
  .contact-phone {
    display: flex;
    align-items: center;
    gap: 10px;
    font-size: 15px;
    margin-top: 28px;
  }
  .contact-phone svg { width: 13px; height: 13px; }
  .emblem-area {
    position: absolute;
    right: -40px;
    bottom: -90px;
    width: 360px;
    height: 300px;
    border-radius: 50% 50% 0 0;
    background: radial-gradient(circle at 55% 70%, var(--faint-trunk) 0%, var(--faint-trunk) 45%, var(--faint-leaf) 70%, rgba(255,255,255,0) 100%);
  }
</style>
</head>
<body>
<main class="stage">
  <section class="card card--front" aria-label="Card front">
    <div class="front-brand">
      <span class="brand-dot"></span>
      <span class="brand-name">Kindred Grove</span>
    </div>
  </section>

  <section class="card card--back" aria-label="Card back">
    <div class="back-brand">Kindred Grove</div>
    <div class="contact">
      <p class="contact-name">Daniel Harrow</p>
      <p class="contact-title">Managing Director</p>
      <p class="contact-phone">
        <svg viewBox="0 0 24 24" aria-hidden="true"><path fill="#1f6b66" d="M6.6 10.8a15.5 15.5 0 0 0 6.6 6.6l2.2-2.2a1 1 0 0 1 1-.25 11.4 11.4 0 0 0 3.6.57 1 1 0 0 1 1 1V20a1 1 0 0 1-1 1A17 17 0 0 1 3 4a1 1 0 0 1 1-1h3.5a1 1 0 0 1 1 1c0 1.25.2 2.45.57 3.57a1 1 0 0 1-.25 1z"/></svg>
        <span>044-555 010 230</span>
      </p>
    </div>
    <div class="emblem-area" role="img" aria-label="Faint tree emblem with leafy canopy, used as a light decoration"></div>
  </section>
</main>
</body>
</html>
```